Tidewell Claimworks Website - a medical billing website - one page

I need a one-page website to attract potential clients to my medical billing services - I am in the process of creating a logo, the contest ends Friday. I also have some ideas and am writing some of the copy that I can send you.

SLOGAN: We Turn Codes Into Money

MISSION STATEMENT: Give compassionate quality service and precision medical billing with urgency

Target Market(s)

MD's, physical therapists, occupational therapists, speech therapists, chiropractors, psychologists, psychiatrists, dentists and new grads of the above

Coding

Coded - Design and coding required

Number of Pages Required

1 page

Font styles to use
Sans Serif
Decorative
Script

Colors
33a6d7
add136
87cfc6
cadf82
9bcb3c
85cae6

Requirements
Must have
• I am working on the major points of copy that I need, plus
• ranking search terms keywords and phrases
Nice to have
• creativity to draw clients in
• my color choices below are similar to the logo coloring - but if you like something different feel free to use your own creative colors.

```html
<!DOCTYPE html>
<html lang="en">
<head>
<meta charset="utf-8">
<title>Tidewell Claimworks — Medical Billing</title>
<link rel="stylesheet" href="https://fonts.googleapis.com/css2?family=Montserrat:wght@300;400;500;600;700&display=swap">
<style>
:root{
  --hero-a:#6fb6d8;
  --hero-b:#4f9ec7;
  --teal:#87cfc6;
  --teal-line:#7fcbc4;
  --sky:#6cb8dc;
  --pale:#eef4f4;
  --ink:#2f2f2f;
  --body:#555a5c;
  --muted:#6a6f71;
  --white:#ffffff;
  --field:#d5d9da;
}
*{box-sizing:border-box;margin:0;padding:0}
html,body{width:1200px;height:3016px;overflow:hidden}
body{position:relative;font-family:"Montserrat",sans-serif;color:var(--body);background:var(--white)}
.abs{position:absolute}
ul{list-style:none}

/* hero */
.hero{left:0;top:0;width:1200px;height:633px;background:linear-gradient(135deg,var(--hero-a),var(--hero-b) 55%,#82c1e0)}
.brand{left:114px;top:24px;font-size:31px;font-weight:400;color:var(--white);letter-spacing:.2px;white-space:nowrap}
.nav{top:37px;font-size:13.5px;font-weight:500;color:var(--white)}
.nav a{position:absolute;white-space:nowrap;color:inherit;text-decoration:none}
.hero-title{left:0;width:1200px;top:106px;text-align:center;font-size:46px;font-weight:700;color:var(--white);letter-spacing:.5px}
.hero-sub{left:0;width:1200px;top:172px;text-align:center;font-size:22.5px;font-weight:400;color:var(--white)}
.hero-btn{left:503px;top:241px;width:196px;height:47px;border:3px solid var(--white);border-radius:24px;color:var(--white);font-size:19px;font-weight:600;display:flex;align-items:center;justify-content:center}
.hero-art{left:421px;top:325px;width:358px;height:260px;border-radius:16px;background:radial-gradient(circle at 50% 50%,rgba(255,255,255,.35),rgba(255,255,255,.08) 70%)}

/* section titles */
.sec-title{left:0;width:1200px;text-align:center;font-size:28px;font-weight:400;color:var(--ink)}
.rule{width:56px;height:3px;background:var(--teal-line)}

/* about */
.about{left:0;top:633px;width:1200px;height:397px;background:var(--pale)}
.about-text{left:173px;width:860px;font-size:14px;line-height:21px;color:var(--body)}

/* why */
.phone-art{left:111px;top:1147px;width:261px;height:384px;background:linear-gradient(160deg,#e7f1ef 0%,#f0dfa8 60%,#ead08e 100%);border-radius:30px 30px 0 0}
.col-head{font-size:17.5px;font-weight:400;color:var(--ink);line-height:21px}
.why-list li{font-size:14.5px;line-height:21.2px;color:var(--body);position:relative;white-space:nowrap}
.why-list li::before{content:"";position:absolute;left:-26px;top:9px;width:4px;height:4px;border-radius:50%;background:var(--body)}
.why-list.tight li::before{left:-13px}

/* services */
.services{left:2px;top:1531px;width:1198px;height:1036px;background:var(--pale)}
.photo{background:linear-gradient(135deg,#e9eef4,#c9d5e3 45%,#f2f4f6)}
.svc-head{font-size:27px;font-weight:300;color:var(--ink);line-height:32px}
.ticks li{position:relative;padding-left:27px;font-size:14.3px;line-height:22.8px;color:var(--body)}
.ticks li svg{position:absolute;left:0;top:5px;width:15px;height:15px}

/* footer */
.foot-brand{left:108px;top:2638px;font-size:26px;font-weight:400;color:var(--sky);white-space:nowrap}
.foot-text{left:111px;top:2690px;width:290px;font-size:14px;line-height:23px;color:var(--muted)}
.contact-item{left:435px;font-size:11.5px;line-height:13px;color:var(--ink);display:flex;align-items:flex-start;gap:18px}
.contact-item svg{flex:none}
.field{border:1px solid var(--field);background:var(--white);font-size:12.5px;color:var(--muted);padding:8px 10px;font-family:inherit}
.send{left:815px;top:2848px;width:147px;height:38px;border-radius:19px;background:#8dd2dc;color:var(--white);font-size:14.5px;font-weight:500;display:flex;align-items:center;justify-content:center}

/* bottom bar */
.bar{left:0;top:2947px;width:1200px;height:69px;background:var(--teal)}
.copy{left:111px;top:2978px;font-size:11.5px;color:var(--white);white-space:nowrap}
.copy b{font-weight:600}
.bar-nav{top:2978px;font-size:11.5px;font-weight:500;color:var(--white);white-space:nowrap}
.to-top{left:1128px;top:2986px;width:53px;height:30px;background:var(--white);border-radius:6px 6px 0 0;display:flex;align-items:center;justify-content:center}
</style>
</head>
<body>

<!-- Hero -->
<section class="abs hero" role="img" aria-label="Blue-tinted photo of a stethoscope resting on a calculator"></section>
<div class="abs brand">Tidewell Claimworks</div>
<nav class="abs nav" style="left:0;width:1200px">
  <a style="left:537px">Home</a>
  <a style="left:622px">About Us</a>
  <a style="left:728px">Our Services</a>
  <a style="left:857px">Why Choose Us?</a>
  <a style="left:1014px">Contact Us</a>
</nav>
<h1 class="abs hero-title">WE TURN CODES INTO MONEY</h1>
<p class="abs hero-sub">We give compassionate quality service and precision medical billing with urgency.</p>
<div class="abs hero-btn">Get started</div>
<div class="abs hero-art" role="img" aria-label="Illustration of a medical team with a heart, clipboard, stethoscope and first aid kit"></div>

<!-- About -->
<section class="abs about"></section>
<h2 class="abs sec-title" style="top:685px">About Us</h2>
<div class="abs rule" style="left:572px;top:738px"></div>
<p class="abs about-text" style="top:777px">We provide professional and quality medical billing services for physicians, psychologists, psychiatrists OT, PT, Speech, and chiropractors.</p>
<p class="abs about-text" style="top:840px">Our dedicated medical billers use multiple software systems to submit medical claims to insurance companies and payers such as Medicare and Medicaid. We will then review and follow up on insurance payments, update insurance information and communicate related information to patients.</p>
<p class="abs about-text" style="top:924px">We communicate with the patient and their insurance company for every medical claim.&nbsp; It frees up internal resources so that you and your staff can focus on what you do best: helping patients.</p>

<!-- Why choose us -->
<div class="abs phone-art" role="img" aria-label="Illustration of a hand holding a smartphone showing a chat screen"></div>
<h2 class="abs sec-title" style="left:430px;width:600px;top:1086px">Why Choose Us?</h2>
<div class="abs rule" style="left:703px;top:1138px"></div>

<svg class="abs" style="left:559px;top:1177px" width="28" height="30" viewBox="0 0 28 30" fill="none" stroke="#7fcbc4" stroke-width="1.4">
  <path d="M14 3 L25 9 L14 15 L3 9 Z"/><path d="M3 14 L14 20 L25 14"/><path d="M3 19 L14 25 L25 19"/>
</svg>
<div class="abs col-head" style="left:427px;top:1218px">We take care of crucial tasks like:</div>
<ul class="abs why-list" style="left:463px;top:1250px">
  <li>Patient Insurance Verification</li>
  <li>Medical Coding</li>
  <li>Claim Tracking</li>
  <li>Billing Analytics &amp; Reports</li>
</ul>

<svg class="abs" style="left:904px;top:1175px" width="32" height="34" viewBox="0 0 32 34" fill="none" stroke="#7fcbc4" stroke-width="1.5">
  <circle cx="16" cy="19" r="13"/><path d="M16 19 V12"/><path d="M13 3 H19"/><path d="M16 3 V6"/><path d="M26 8 L28 6"/>
</svg>
<div class="abs col-head" style="left:768px;top:1218px;width:300px">Benefits of outsourcing medical billing</div>
<ul class="abs why-list tight" style="left:781px;top:1275px">
  <li>Simplifying financial record-keeping</li>
  <li>Data protection for sensitive files</li>
  <li>High accuracy</li>
  <li>Quick turnaround time for insurance claims</li>
  <li>Scalability</li>
</ul>

<!-- Services -->
<section class="abs services"></section>
<h2 class="abs sec-title" style="top:1583px">Our Services</h2>
<div class="abs rule" style="left:574px;top:1636px"></div>

<div class="abs photo" style="left:0;top:1698px;width:549px;height:372px" role="img" aria-label="Photo of a doctor in a white coat writing notes on paperwork at a desk"></div>
<div class="abs svc-head" style="left:603px;top:1692px;width:520px">Our team of qualified billers are standing by, ready to:</div>
<ul class="abs ticks" style="left:603px;top:1775px;width:560px">
  <li><svg viewBox="0 0 16 16" fill="none" stroke="#7fcbc4" stroke-width="1.4"><path d="M14 7.4V8a6 6 0 1 1-3.6-5.5"/><path d="M14 3 8 9 6 7"/></svg>Actively follow up on all assigned accounts.</li>
  <li><svg viewBox="0 0 16 16" fill="none" stroke="#7fcbc4" stroke-width="1.4"><path d="M14 7.4V8a6 6 0 1 1-3.6-5.5"/><path d="M14 3 8 9 6 7"/></svg>Timely management of a large volume of claims.</li>
  <li><svg viewBox="0 0 16 16" fill="none" stroke="#7fcbc4" stroke-width="1.4"><path d="M14 7.4V8a6 6 0 1 1-3.6-5.5"/><path d="M14 3 8 9 6 7"/></svg>Entering demographics, and charges into our billing software.</li>
  <li><svg viewBox="0 0 16 16" fill="none" stroke="#7fcbc4" stroke-width="1.4"><path d="M14 7.4V8a6 6 0 1 1-3.6-5.5"/><path d="M14 3 8 9 6 7"/></svg>Submit claim resubmissions to insurance carriers.</li>
  <li><svg viewBox="0 0 16 16" fill="none" stroke="#7fcbc4" stroke-width="1.4"><path d="M14 7.4V8a6 6 0 1 1-3.6-5.5"/><path d="M14 3 8 9 6 7"/></svg>Follow-up on unpaid claims and underpaid claims.</li>
  <li><svg viewBox="0 0 16 16" fill="none" stroke="#7fcbc4" stroke-width="1.4"><path d="M14 7.4V8a6 6 0 1 1-3.6-5.5"/><path d="M14 3 8 9 6 7"/></svg>Review daily remittance advice for denials.</li>
  <li><svg viewBox="0 0 16 16" fill="none" stroke="#7fcbc4" stroke-width="1.4"><path d="M14 7.4V8a6 6 0 1 1-3.6-5.5"/><path d="M14 3 8 9 6 7"/></svg>Knowledge of PPO and HMO, MEDI-CAL and MEDI-CAL affiliated plans.</li>
  <li><svg viewBox="0 0 16 16" fill="none" stroke="#7fcbc4" stroke-width="1.4"><path d="M14 7.4V8a6 6 0 1 1-3.6-5.5"/><path d="M14 3 8 9 6 7"/></svg>Knowledgeable in Appeals process.</li>
  <li><svg viewBox="0 0 16 16" fill="none" stroke="#7fcbc4" stroke-width="1.4"><path d="M14 7.4V8a6 6 0 1 1-3.6-5.5"/><path d="M14 3 8 9 6 7"/></svg>Strong organizational and attention to details skills.</li>
  <li><svg viewBox="0 0 16 16" fill="none" stroke="#7fcbc4" stroke-width="1.4"><path d="M14 7.4V8a6 6 0 1 1-3.6-5.5"/><path d="M14 3 8 9 6 7"/></svg>Demonstrated knowledge and respect the Laws of HIPAA rules and regulations.</li>
</ul>

<div class="abs svc-head" style="left:52px;top:2113px">Add ons:</div>
<ul class="abs ticks" style="left:51px;top:2162px;width:540px">
  <li><svg viewBox="0 0 16 16" fill="none" stroke="#7fcbc4" stroke-width="1.4"><path d="M14 7.4V8a6 6 0 1 1-3.6-5.5"/><path d="M14 3 8 9 6 7"/></svg>Communicate with all insurance companies, patients and providers.</li>
  <li><svg viewBox="0 0 16 16" fill="none" stroke="#7fcbc4" stroke-width="1.4"><path d="M14 7.4V8a6 6 0 1 1-3.6-5.5"/><path d="M14 3 8 9 6 7"/></svg>Verify and confirm proper coverage through eligibility and benefit verification.</li>
  <li><svg viewBox="0 0 16 16" fill="none" stroke="#7fcbc4" stroke-width="1.4"><path d="M14 7.4V8a6 6 0 1 1-3.6-5.5"/><path d="M14 3 8 9 6 7"/></svg>Utilize EHR software to document communications on collection activity, with insurance companies and patients.</li>
  <li><svg viewBox="0 0 16 16" fill="none" stroke="#7fcbc4" stroke-width="1.4"><path d="M14 7.4V8a6 6 0 1 1-3.6-5.5"/><path d="M14 3 8 9 6 7"/></svg>Ensure RAPs are reprocessed within 24 hours of cancellation.</li>
  <li><svg viewBox="0 0 16 16" fill="none" stroke="#7fcbc4" stroke-width="1.4"><path d="M14 7.4V8a6 6 0 1 1-3.6-5.5"/><path d="M14 3 8 9 6 7"/></svg>Research and analyze patient account activity to maintain accuracy of patient account balances.</li>
  <li><svg viewBox="0 0 16 16" fill="none" stroke="#7fcbc4" stroke-width="1.4"><path d="M14 7.4V8a6 6 0 1 1-3.6-5.5"/><path d="M14 3 8 9 6 7"/></svg>Receive, review and log all incoming batches.</li>
  <li><svg viewBox="0 0 16 16" fill="none" stroke="#7fcbc4" stroke-width="1.4"><path d="M14 7.4V8a6 6 0 1 1-3.6-5.5"/><path d="M14 3 8 9 6 7"/></svg>Monitors staff for compliance with HIPAA regulations and maintaining strictest confidentiality.</li>
</ul>
<div class="abs photo" style="left:650px;top:2118px;width:550px;height:372px;background:linear-gradient(135deg,#d9cbb3,#6d7f93 50%,#b9c6d6)" role="img" aria-label="Photo of two women seated on a sofa in conversation"></div>

<!-- Footer -->
<div class="abs foot-brand">Tidewell Claimworks</div>
<p class="abs foot-text">Gift yourself the opportunity to grow your practice while our amazing team of caring and talented professionals provide quality medical billing services.</p>

<div class="abs contact-item" style="top:2640px">
  <svg width="20" height="26" viewBox="0 0 20 26" fill="none" stroke="#7fcbc4" stroke-width="1.3"><path d="M10 25S2 15 2 9.5a8 8 0 0 1 16 0C18 15 10 25 10 25Z"/><circle cx="10" cy="9.5" r="3"/></svg>
  <span style="margin-top:7px">Your address,<br>Street name<br>Zip code</span>
</div>
<div class="abs contact-item" style="top:2729px">
  <svg width="22" height="16" viewBox="0 0 22 16" fill="none" stroke="#7fcbc4" stroke-width="1.3"><rect x="1" y="1" width="20" height="14"/><path d="M1 1 11 9 21 1"/></svg>
  <span style="margin-top:2px">info@tidewellclaimworks.com</span>
</div>
<div class="abs contact-item" style="top:2789px">
  <svg width="22" height="22" viewBox="0 0 22 22" fill="none" stroke="#7fcbc4" stroke-width="1.3"><path d="M5 2 8 7 6 9c1 3 4 6 7 7l2-2 5 3-2 4C10 21 1 12 1 4Z"/></svg>
  <span style="margin-top:7px">+011 5550 4172</span>
</div>

<div class="abs field" style="left:691px;top:2639px;width:193px;height:31px">Your Name</div>
<div class="abs field" style="left:892px;top:2639px;width:194px;height:31px">Your Email</div>
<div class="abs field" style="left:691px;top:2683px;width:395px;height:31px">Subject</div>
<div class="abs field" style="left:691px;top:2729px;width:395px;height:106px">Message</div>
<div class="abs send">Send message</div>

<!-- Bottom bar -->
<div class="abs bar"></div>
<div class="abs copy">© Copyright <b>Tidewell Claimworks</b>. All Rights Reserved</div>
<div class="abs bar-nav" style="left:706px">Home</div>
<div class="abs bar-nav" style="left:757px">About Us</div>
<div class="abs bar-nav" style="left:826px">Our Services</div>
<div class="abs bar-nav" style="left:914px">Why Choose Us?</div>
<div class="abs bar-nav" style="left:1026px">Contact Us</div>
<div class="abs to-top">
  <svg width="16" height="10" viewBox="0 0 16 10" fill="none" stroke="#555" stroke-width="2"><path d="M2 8 8 2 14 8"/></svg>
</div>

</body>
</html>
```